Poetry Book Cover Design Project

Looking for a minimalistic book cover design for a collection of poems. The book title is "Where The Lanterns Drift Slowly Apart". There are three parts to the book. First covers poetry in the theme of Rage. Second love and desire. The third is strange poems. Essentially the sections are "Rage", "Desire" and the "Strange". The reason for the title "Where The Lanterns Drift Slowly Apart" is as if someone is writing these till life changes towards the intended outcome as felt in each poem. I want to have the author's name "Nuwanthi Karunasekera" at the bottom. Ilustration attached.
- Minimalistic

```html
<!DOCTYPE html>
<html lang="en">
<head>
<meta charset="utf-8">
<title>Where The Lanterns Drift Slowly Apart — Book Cover</title>
<link href="https://fonts.googleapis.com/css2?family=Crimson+Pro:ital,wght@0,400;1,400&family=Parisienne&display=swap" rel="stylesheet">
<style>
  :root {
    --backdrop: #e8edf1;
    --paper: #f7f6f1;
    --paper-shade: #ecebe4;
    --title-violet: #4a3aa6;
    --author-plum: #9a2356;
    --author-rose: #b2577f;
    --orchid-peach: #f0a585;
    --orchid-salmon: #e58f78;
    --orchid-gold: #f1d27a;
    --leaf-green: #9dbb86;
  }
  * { margin: 0; padding: 0; box-sizing: border-box; }
  html, body {
    width: 1200px;
    height: 800px;
    overflow: hidden;
    background: var(--backdrop);
  }
  .stage {
    width: 1200px;
    height: 800px;
    display: flex;
    align-items: center;
    justify-content: center;
  }
  .cover {
    position: relative;
    width: 480px;
    height: 722px;
    overflow: hidden;
    background: linear-gradient(160deg, var(--paper) 0%, var(--paper) 55%, var(--paper-shade) 100%);
    box-shadow: 0 6px 24px rgba(60, 80, 100, 0.18);
  }
  .orchid-spray {
    position: absolute;
    left: 0;
    top: 0;
    width: 256px;
    height: 134px;
    border-radius: 0 0 60% 10% / 0 0 90% 40%;
    background:
      radial-gradient(ellipse 40% 45% at 30% 40%, var(--orchid-gold) 0%, transparent 60%),
      radial-gradient(ellipse 70% 80% at 40% 35%, var(--orchid-peach) 0%, rgba(240,165,133,0.6) 55%, transparent 100%),
      radial-gradient(ellipse 30% 30% at 85% 30%, var(--leaf-green) 0%, transparent 80%);
    opacity: 0.9;
  }
  .orchid-bloom {
    position: absolute;
    right: 0;
    bottom: 0;
    width: 250px;
    height: 295px;
    border-radius: 55% 0 0 0 / 50% 0 0 0;
    background:
      radial-gradient(ellipse 30% 35% at 40% 45%, var(--orchid-gold) 0%, transparent 80%),
      radial-gradient(ellipse 80% 85% at 55% 55%, var(--orchid-salmon) 0%, rgba(229,143,120,0.55) 65%, transparent 100%);
  }
  .title {
    position: absolute;
    right: 34px;
    top: 262px;
    text-align: right;
    color: var(--title-violet);
    line-height: 1;
  }
  .title-script {
    display: block;
    font-family: "Parisienne", cursive;
    font-size: 44px;
  }
  .title-link {
    display: block;
    margin-top: 4px;
    padding-right: 56px;
    font-family: "Crimson Pro", serif;
    font-style: italic;
    font-size: 31px;
  }
  .title-main {
    display: block;
    margin-top: 2px;
    padding-right: 4px;
    font-family: "Crimson Pro", serif;
    font-size: 43px;
  }
  .author {
    position: absolute;
    left: 21px;
    top: 572px;
    font-family: "Crimson Pro", serif;
    font-style: italic;
    font-size: 30px;
    line-height: 1.35;
  }
  .author-first { display: block; color: var(--author-plum); }
  .author-last { display: block; color: var(--author-rose); }
</style>
</head>
<body>
  <main class="stage">
    <section class="cover">
      <div class="orchid-spray" role="img" aria-label="Watercolour spray of peach orchids with green leaves"></div>
      <div class="orchid-bloom" role="img" aria-label="Large close-up salmon orchid bloom with a speckled yellow lip"></div>
      <h1 class="title">
        <span class="title-script">Where The Lanterns</span>
        <span class="title-link">Drift Slowly</span>
        <span class="title-main">Apart</span>
      </h1>
      <p class="author">
        <span class="author-first">Nuwanthi</span>
        <span class="author-last">Karunasekera</span>
      </p>
    </section>
  </main>
</body>
</html>
```